Poster Design

Hello,

My name is Rowan Pickett and I run a vidora channel called 'CrumbleDiary'. I want a poster made for those who watch my video to purchase and put on their wall at home. The poster will be all text and as you can see, I've attached a few examples of posters which I would like it to be similar to. I use a lot of the colour #ab6f7f so it would be good to incorporate this in somewhere (maybe the background colour).
I would like the poster to say:
"Do More Of What Makes YOU Happy"
I need this poster to be for sale ready for christmas, so Im going to need the designs created as soon as possible. Im sorry for the rush.
Have fun with it and feel free to upload multiple versions of a design as well as a few designs if you like.
I look forward to seeing what you come up with.
Rowan
(Of course I will need to own all rights once the payment has been made)

```html
<!DOCTYPE html>
<html lang="en">
<head>
<meta charset="utf-8">
<title>Do More of What Makes You Happy — Poster</title>
<link rel="stylesheet" href="https://fonts.googleapis.com/css2?family=Ultra&family=Playfair+Display:ital,wght@1,900&display=swap">
<style>
  :root {
    --paper: #fdf5ea;
    --mauve: #ab6f7f;
    --mint: #1eea84;
    --white: #ffffff;
  }
  html, body {
    margin: 0;
    padding: 0;
    width: 849px;
    height: 1200px;
    overflow: hidden;
    background: var(--paper);
  }
  .poster {
    display: block;
    width: 849px;
    height: 1200px;
  }
  .poster__panel { fill: var(--mauve); }
  .quote-line {
    font-family: "Ultra", Georgia, serif;
    fill: var(--mint);
  }
  .quote-line--accent { fill: var(--white); }
  .quote-line--small {
    font-family: "Playfair Display", Georgia, serif;
    font-style: italic;
    font-weight: 900;
  }
  .quote-mark {
    font-family: "Ultra", Georgia, serif;
    fill: none;
    stroke: var(--mint);
    stroke-width: 4;
  }
</style>
</head>
<body>
<svg class="poster" viewBox="0 0 849 1200" xmlns="http://www.w3.org/2000/svg">
  <path class="poster__panel" d="M24 24 L300 21 L560 25 L826 22 L823 300 L828 620 L824 900 L828 1168 L540 1166 L260 1170 L22 1167 L26 880 L21 560 L25 260 Z"/>

  <text class="quote-mark" x="66" y="290" font-size="230" textLength="95" lengthAdjust="spacingAndGlyphs">&#8220;</text>

  <text class="quote-line" x="162" y="300" font-size="200" textLength="280" lengthAdjust="spacingAndGlyphs">Do</text>
  <text class="quote-line" x="158" y="452" font-size="205" textLength="495" lengthAdjust="spacingAndGlyphs">More</text>
  <text class="quote-line quote-line--small" x="163" y="540" font-size="78" textLength="80" lengthAdjust="spacingAndGlyphs">of</text>
  <text class="quote-line" x="288" y="597" font-size="195" textLength="402" lengthAdjust="spacingAndGlyphs">What</text>
  <text class="quote-line" x="155" y="698" font-size="135" textLength="537" lengthAdjust="spacingAndGlyphs">Makes</text>
  <text class="quote-line quote-line--accent" x="158" y="840" font-size="240" textLength="532" lengthAdjust="spacingAndGlyphs">you</text>
  <text class="quote-line" x="288" y="972" font-size="108" textLength="385" lengthAdjust="spacingAndGlyphs">Happy</text>

  <text class="quote-mark" x="694" y="1040" font-size="230" textLength="90" lengthAdjust="spacingAndGlyphs">&#8221;</text>
</svg>
</body>
</html>
```